professional looking data specialist website

I've recently had a new logo designed and I'm now looking to get a professional looking website built. This is for a new company that specialises in data. We look to support companies with business intelligence, report modelling, data governance to new european legislation (GDPR). We are offer consultancy or we can attend site and complete work when required. Our target arket is united kingdom wide and we are specifically aiming at small to medium sized companies.

Target Market(s)

small to medium enterprise companies from all industries

Industry/Entity Type

Professional Service

Coding

Coded - Design and coding required

Number of Pages Required

4 page

Font styles to use
Sans Serif

Colors

Designer to choose colors to be used in the design.

Requirements
Must have
• Professional look including the company logo, need to have ability to request more information from us so needs a inquiries page, seperate pages for the different offerings, data governance, report modelling, business intelligence implementation, data protection
Nice to have
• any website interaction, animation, etc
Should not have
• too many colours, too busy pages, must look professional

```html
<!DOCTYPE html>
<html lang="en">
<head>
<meta charset="utf-8">
<title>Harwell Data Ltd</title>
<link href="https://fonts.googleapis.com/css2?family=Raleway:wght@500;600;700&family=Arimo:wght@400;700&display=swap" rel="stylesheet">
<style>
:root{
  --blue:#1670c2;
  --blue-dark:#0f5ea8;
  --ink:#4a4a4a;
  --muted:#666;
  --light:#efefef;
  --footer:#2b2b2b;
  --field:#3a3a3a;
  --icon-tint:#dceaf6;
}
*{box-sizing:border-box;margin:0;padding:0}
html,body{width:744px;height:1200px;overflow:hidden}
body{position:relative;background:#fff;font-family:'Arimo',Arial,sans-serif;color:var(--ink)}
.abs{position:absolute}
.head{font-family:'Raleway',sans-serif}

/* header */
.site-header{left:0;top:0;width:744px;height:84px;border-top:2px solid var(--blue);background:#fff}
.brand{left:50px;top:46px;display:flex;align-items:center;gap:7px;font-family:'Raleway',sans-serif;font-weight:600;font-size:20px;color:var(--blue)}
.brand-square{width:14px;height:14px;background:var(--blue)}
.top-phone{left:478px;top:14px;display:flex;align-items:center;gap:5px;font-family:'Raleway',sans-serif;font-weight:600;font-size:11.5px;color:#555}
.top-mail{left:619px;top:18px;font-size:7.5px;color:#555}
.nav{top:60px;font-size:10.5px;font-family:'Raleway',sans-serif;font-weight:600;color:#555}
.nav.active{color:var(--blue)}
.nav-sep{top:62px;width:1px;height:9px;background:#ddd}

/* hero */
.hero{left:0;top:84px;width:744px;height:312px;background:linear-gradient(115deg,#0b2a45 0%,#124c78 35%,#0e3553 60%,#1b2430 100%)}
.hero-caption{left:0;top:350px;width:744px;height:46px;background:rgba(0,0,0,.35);color:#fff;text-align:center;font-family:'Raleway',sans-serif;font-weight:700;font-size:15.5px;line-height:19px;padding-top:4px}
.arrow{top:209px;width:25px;height:23px;background:rgba(60,60,60,.85);border:1px solid #999}

/* services */
.section-title{left:0;width:744px;text-align:center;font-family:'Raleway',sans-serif;font-weight:600;font-size:20px;color:#555}
.section-title span{color:var(--blue)}
.rule{left:347px;width:50px;height:1px;background:#aaa}
.service{width:140px;text-align:center}
.service h3{font-family:'Raleway',sans-serif;font-weight:700;font-size:12.5px;line-height:14.5px;color:var(--blue);height:32px}
.service p{margin-top:8px;font-size:7.8px;line-height:11.5px;color:var(--muted)}
.service p b{color:var(--blue)}
.service svg{display:block;margin:0 auto 12px}

/* welcome */
.welcome{left:0;top:742px;width:744px;height:198px;background:var(--light)}
.welcome-text{left:60px;top:818px;width:624px;text-align:center;font-size:9px;line-height:14.2px;color:#333}
.btn-more{left:331px;top:887px;width:78px;height:21px;background:#8c8c8c;color:#fff;font-family:'Raleway',sans-serif;font-weight:600;font-size:9.5px;line-height:21px;padding-left:7px}

/* footer */
.footer{left:0;top:940px;width:744px;height:232px;background:var(--footer)}
.foot-title{font-family:'Raleway',sans-serif;font-weight:600;font-size:14px;color:#fff}
.field{left:51px;width:187px;border:1px solid #999;font-size:7.5px;color:#ddd;padding:3px 7px}
.send{left:51px;top:1129px;width:61px;height:19px;background:var(--blue);color:#fff;font-size:8.5px;font-weight:700;text-align:center;line-height:19px}
.vdiv{top:990px;width:1px;height:130px;background:#3c3c3c}
.map{left:296px;top:1010px;width:188px;height:114px;background:linear-gradient(135deg,#e8e1cf 0%,#cfdff0 45%,#a9c8e6 60%,#e5dcc6 100%)}
.contact-item{left:541px;display:flex;gap:9px;font-size:8.3px;line-height:11.5px;color:#fff}
.contact-item svg{flex:none;margin-top:1px}
.copyright{left:0;top:1172px;width:744px;height:28px;background:var(--blue);color:#fff;text-align:center;font-family:'Raleway',sans-serif;font-weight:700;font-size:9px;line-height:28px}
</style>
</head>
<body>

<header class="abs site-header"></header>
<div class="abs brand"><span class="brand-square"></span>Harwell Data Ltd</div>
<div class="abs top-phone">
  <svg width="18" height="18" viewBox="0 0 18 18"><rect x="1" y="1" width="16" height="16" rx="2" fill="none" stroke="#999"/><path d="M6 5c-1 1 0 4 2 6s5 3 6 2l-1.5-1.5-1.5 1c-1-.5-2.5-2-3-3l1-1.5z" fill="var(--blue)"/></svg>
  (123)-456-7890
</div>
<div class="abs top-mail">info@harwelldata.com</div>
<div class="abs nav active" style="left:402px">Home</div>
<div class="abs nav-sep" style="left:452px"></div>
<div class="abs nav" style="left:473px">About Us</div>
<div class="abs nav-sep" style="left:537px"></div>
<div class="abs nav" style="left:558px">Services</div>
<div class="abs nav-sep" style="left:619px"></div>
<div class="abs nav" style="left:640px">Contact Us</div>

<section class="abs hero" role="img" aria-label="Hand holding glowing hexagonal technology icons in front of server racks"></section>
<div class="abs hero-caption">Offering Consultancy Services From Small To Medium EnterprisesCompanies To All<br>Industries In The UK</div>
<div class="abs arrow" style="left:3px"><svg width="23" height="21" viewBox="0 0 23 21"><path d="M13 6l-4 4.5 4 4.5" fill="none" stroke="#fff" stroke-width="2"/></svg></div>
<div class="abs arrow" style="left:715px"><svg width="23" height="21" viewBox="0 0 23 21"><path d="M10 6l4 4.5-4 4.5" fill="none" stroke="#fff" stroke-width="2"/></svg></div>

<h2 class="abs section-title" style="top:422px">Our <span>Services</span></h2>
<div class="abs rule" style="top:457px"></div>

<div class="abs service" style="left:56px;top:520px">
  <svg width="60" height="96" viewBox="0 0 60 96"><rect x="5" y="20" width="22" height="9" rx="2" fill="var(--blue)"/><rect x="5" y="32" width="22" height="9" rx="2" fill="var(--blue)"/><rect x="5" y="44" width="22" height="9" rx="2" fill="var(--blue)"/><circle cx="40" cy="44" r="11" fill="none" stroke="var(--blue)" stroke-width="5"/><path d="M44 28l6 5-7 3z" fill="var(--blue)"/></svg>
  <h3>Data<br>Governance</h3>
  <p>Lorem ipsum dolor sit amet, consectetuer adipiscing elit, sed diam nonummy nibh euismo...<b>{+}</b></p>
</div>
<div class="abs service" style="left:220px;top:520px">
  <svg width="60" height="96" viewBox="0 0 60 96"><rect x="8" y="12" width="42" height="56" fill="#fff" stroke="var(--blue)" stroke-width="2"/><rect x="12" y="16" width="34" height="5" fill="var(--blue)"/><circle cx="17" cy="29" r="4" fill="none" stroke="var(--blue)" stroke-width="1.5"/><rect x="24" y="26" width="20" height="5" fill="var(--blue)"/><rect x="13" y="36" width="8" height="8" fill="none" stroke="var(--blue)" stroke-width="1.5"/><rect x="24" y="37" width="20" height="3" fill="var(--blue)"/><rect x="24" y="47" width="20" height="3" fill="var(--blue)"/><rect x="24" y="55" width="20" height="3" fill="var(--blue)"/><rect x="13" y="47" width="8" height="10" fill="var(--blue)"/></svg>
  <h3>Report<br>Modeling</h3>
  <p>Lorem ipsum dolor sit amet, consectetuer adipiscing elit, sed diam nonummy nibh euismo...<b>{+}</b></p>
</div>
<div class="abs service" style="left:383px;top:520px">
  <svg width="60" height="96" viewBox="0 0 60 96"><rect x="8" y="44" width="6" height="14" fill="var(--blue)"/><rect x="17" y="38" width="6" height="20" fill="var(--blue)"/><rect x="26" y="33" width="6" height="25" fill="var(--blue)"/><rect x="35" y="27" width="6" height="31" fill="var(--blue)"/><path d="M6 40l14-10 8 5 16-15" fill="none" stroke="var(--blue)" stroke-width="3"/><path d="M40 16l10-4-3 10z" fill="var(--blue)"/></svg>
  <h3>Business Intelligence<br>Implementation</h3>
  <p>Lorem ipsum dolor sit amet, consectetuer adipiscing elit, sed diam nonummy nibh euismo...<b>{+}</b></p>
</div>
<div class="abs service" style="left:547px;top:520px">
  <svg width="60" height="96" viewBox="0 0 60 96"><ellipse cx="26" cy="24" rx="17" ry="6" fill="var(--blue)"/><rect x="9" y="28" width="34" height="8" rx="3" fill="var(--blue)"/><rect x="9" y="38" width="34" height="8" rx="3" fill="var(--blue)"/><rect x="9" y="48" width="34" height="8" rx="3" fill="var(--blue)"/><circle cx="45" cy="51" r="9" fill="var(--blue)" stroke="#fff" stroke-width="2"/><rect x="41.5" y="50" width="7" height="6" fill="#fff"/><path d="M43 50v-2a2 2 0 0 1 4 0v2" fill="none" stroke="#fff" stroke-width="1.3"/></svg>
  <h3>Data<br>Protection</h3>
  <p>Lorem ipsum dolor sit amet, consectetuer adipiscing elit, sed diam nonummy nibh euismo...<b>{+}</b></p>
</div>

<section class="abs welcome"></section>
<h2 class="abs section-title" style="top:770px">Welcome To <span>Harwell Data</span> Ltd</h2>
<div class="abs rule" style="top:804px"></div>
<p class="abs welcome-text">Lorem ipsum dolor sit amet, consectetuer adipiscing elit, sed diam nonummy nibh euismod tincidunt ut laoreet dolore magna aliquam erat volutpat. Ut wisi enim ad minim veniam, quis nostrud exerci tation ullamcorper suscipit lobortis nisl ut aliquip ex ea commodo consequat. Duis autem vel eum iriure dolor in hendrerit in vulputate velit esse molestie consequat, vel illum dolore eu feugiat nulla facilisis at vero eros et accumsan et iusto odio dignissim qui blandit praesent luptatum zzril delenit augue duis dolore te feugait nulla facilisi.</p>
<div class="abs btn-more">Read More</div>

<footer class="abs footer"></footer>
<h3 class="abs foot-title" style="left:52px;top:974px">Quick Inquiry</h3>
<div class="abs field" style="top:1011px;height:17px">Name</div>
<div class="abs field" style="top:1032px;height:16px">Email</div>
<div class="abs field" style="top:1052px;height:16px">Subject</div>
<div class="abs field" style="top:1072px;height:50px">Message</div>
<div class="abs send">SEND</div>
<div class="abs vdiv" style="left:265px"></div>

<h3 class="abs foot-title" style="left:296px;top:972px">Location Map</h3>
<div class="abs map" role="img" aria-label="Street map showing the office location"></div>
<div class="abs vdiv" style="left:510px"></div>

<h3 class="abs foot-title" style="left:548px;top:982px">Contact Details</h3>
<div class="abs contact-item" style="top:1010px"><svg width="8" height="11" viewBox="0 0 8 11"><path d="M4 0a4 4 0 0 1 4 4c0 3-4 7-4 7S0 7 0 4a4 4 0 0 1 4-4z" fill="var(--blue)"/><circle cx="4" cy="4" r="1.5" fill="var(--footer)"/></svg><span>Loren ipsum dolor sit amet mbert<br>Quayside, Leeds LS1 4AB.</span></div>
<div class="abs contact-item" style="top:1044px"><svg width="9" height="9" viewBox="0 0 9 9"><path d="M1 0l2 2-1 1.5c.6 1.4 2 2.9 3.5 3.5L7 6l2 2-1 1C4 9 0 5 0 1z" fill="var(--blue)"/></svg><span>123-456-7890</span></div>
<div class="abs contact-item" style="top:1069px"><svg width="9" height="9" viewBox="0 0 9 9"><rect x="2" y="0" width="5" height="3" fill="var(--blue)"/><rect x="0" y="3" width="9" height="4" fill="var(--blue)"/><rect x="2" y="6" width="5" height="3" fill="var(--blue)"/></svg><span>123-456-7890</span></div>
<div class="abs contact-item" style="top:1094px"><svg width="9" height="7" viewBox="0 0 9 7"><rect width="9" height="7" fill="var(--blue)"/><path d="M0 0l4.5 4L9 0" fill="none" stroke="var(--footer)"/></svg><span>info@harwelldata.com</span></div>

<div class="abs copyright">Copyright © 2017 Harwell Data Ltd . All Right Reserved</div>

</body>
</html>
```